Serene Spiritual Website Wanted for World Wide Organisation

We need a serene, clean web design for our organisation that works around the world.

What We Do
We aim to bring life into synergy across the world. We inspire, motivate, synchronise, and harmonise. We work with energy which is essential to all of life (environmental, human & animal). Our website must depict the spiritual element of being innately natural and reflect animism.

We have included a PDF attachment with details of the structure, navigation, and some websites for ideas/reference. The logo is also attached.
Updates

Target Market(s)

Anyone over 18yrs looking for answers to life's big questions or looking to develop themselves

Industry/Entity Type

Spiritual/wellbeing/Self Development

Number of Pages Required

5+ page

Requirements
Must have
• It must be serene and natural looking, it must incorporate the logo.
Nice to have
• We have included a Powerpoint document which may help you understand what we need, it is just an idea for structure and style, it is not set in stone so feel free to be as creative as you like!
Should not have
• Not clinical.

```html
<!DOCTYPE html>
<html lang="en">
<head>
<meta charset="utf-8">
<title>Lumenara — Shop</title>
<link href="https://fonts.googleapis.com/css2?family=Mulish:wght@400;600;700&display=swap" rel="stylesheet">
<style>
:root{
  --navy:#3e3e68;
  --ink:#4a4a66;
  --gold:#c9a94a;
  --star:#f0d052;
  --panel:#f1f1f4;
  --white:#ffffff;
  --line:#3e3e68;
}
*{margin:0;padding:0;box-sizing:border-box}
html,body{width:692px;height:1200px;overflow:hidden;background:var(--white)}
body{position:relative;font-family:'Mulish',sans-serif;color:var(--ink)}
.hero{position:absolute;left:0;top:0;width:692px;height:181px;
  background:linear-gradient(180deg,#e0cf86 0%,#d8d0a8 30%,#cfccc4 65%,#dcdad8 100%)}
.hero-photo{position:absolute;inset:0;
  background:radial-gradient(ellipse 80px 90px at 470px 95px,rgba(150,155,160,.55),rgba(150,155,160,0) 100%),
             linear-gradient(160deg,rgba(255,255,255,0) 40%,rgba(200,198,205,.4) 100%)}
.brand{position:absolute;left:67px;top:12px;width:70px;text-align:center}
.brand-mark{width:20px;height:20px;border-radius:50%;background:var(--navy);margin:0 auto 4px}
.brand-name{font-size:9px;font-weight:700;letter-spacing:.8px;color:var(--gold);text-transform:uppercase}
.nav{position:absolute;top:26px;font-size:7.5px;color:var(--ink)}
.nav a{position:absolute;white-space:nowrap;color:inherit;text-decoration:none}
.nav a.active{font-weight:700;color:var(--navy)}
.hero-title{position:absolute;right:66px;top:82px;font-size:36px;font-weight:600;color:var(--navy)}
.sort{position:absolute;left:506px;top:224px;font-size:8.7px;font-weight:600;color:var(--navy)}
.sort-select{position:absolute;left:543px;top:219px;width:81px;height:22px;border:1px solid #9a9aaa;
  font-size:7.5px;padding:6px 0 0 13px;color:var(--ink)}
.sort-select svg{position:absolute;right:13px;top:9px}
.categories{position:absolute;left:67px;top:253px;width:96px;height:122px;background:var(--panel);padding:14px 0 0 11px}
.categories h3{font-size:8.7px;font-weight:700;color:var(--navy)}
.categories .rule{width:26px;height:1px;background:var(--gold);margin:6px 0 7px}
.categories li{list-style:none;font-size:8.7px;height:23.5px;color:var(--ink)}
.grid{position:absolute;left:205px;top:255px;display:grid;grid-template-columns:repeat(3,128px);column-gap:14px;row-gap:18px}
.card{position:relative;width:128px;height:218px;background:var(--white);box-shadow:0 1px 4px rgba(60,60,90,.14)}
.card-image{height:93px}
.img-mala{background:radial-gradient(circle at 48% 48%,#b87a34 0%,#c98d44 35%,#f3f0ec 70%,#fafafa 100%)}
.img-book{background:radial-gradient(ellipse 32px 40px at 50% 45%,#d56fa0 0%,#e7b04f 40%,#8ec6e0 70%,#ffffff 100%)}
.img-bracelet{background:linear-gradient(90deg,#e6e8ec 0%,#ecdcd2 50%,#b77a4a 85%,#e4e6ea 100%)}
.card-body{position:absolute;left:16px;top:105px;width:108px}
.card-title{font-size:8.4px;font-weight:600;color:var(--navy)}
.card-price{font-size:7.5px;margin-top:5px}
.card-desc{font-size:7.2px;line-height:9.6px;margin-top:3px}
.stars{display:flex;gap:3.5px;margin-top:9px}
.btn{position:absolute;left:14px;top:176px;width:68px;height:22px;border:1.2px solid var(--line);
  font-size:7.5px;text-align:center;line-height:20px;color:var(--ink)}
.footer{position:absolute;left:0;top:1017px;width:692px;height:183px;background:var(--navy);color:#e8e8f2}
.footer-brand{position:absolute;left:67px;top:33px;width:82px;text-align:center}
.footer-brand .brand-mark{width:34px;height:34px;background:#5a5a86;margin-bottom:7px}
.footer-brand .brand-name{font-size:10px}
.footer-about{position:absolute;left:67px;top:101px;width:170px;font-size:6.2px;line-height:12px}
.footer-rule{position:absolute;left:67px;top:136px;width:37px;height:1px;background:var(--gold)}
.copyright{position:absolute;left:67px;top:144px;font-size:6.2px}
.footer-col{position:absolute;top:34px}
.footer-col h4{font-size:7.5px;font-weight:700;color:#fff}
.footer-col .rule{width:26px;height:1px;background:var(--gold);margin:5px 0 6px}
.footer-col li{list-style:none;font-size:6.4px;height:18px}
.socials{display:flex;gap:10px}
.socials span{width:14px;height:14px;border-radius:50%;background:#fff}
</style>
</head>
<body>
<header class="hero">
  <div class="hero-photo" role="img" aria-label="Stacked smooth stones on raked sand"></div>
  <div class="brand"><div class="brand-mark"></div><div class="brand-name">Lumenara</div></div>
  <nav class="nav">
    <a style="left:401px">Events</a>
    <a style="left:442px">About</a>
    <a style="left:482px">Synchronise Life</a>
    <a style="left:558px">Wisdom</a>
    <a class="active" style="left:606px">Shop</a>
  </nav>
  <h1 class="hero-title">Shop</h1>
</header>

<div class="sort">Sort by</div>
<div class="sort-select">Best Selling
  <svg width="6" height="4" viewBox="0 0 6 4"><path d="M.5.5 3 3 5.5.5" fill="none" stroke="#4a4a66" stroke-width=".9"/></svg>
</div>

<aside class="categories">
  <h3>Shop by Category</h3>
  <div class="rule"></div>
  <ul><li>Malas</li><li>Arts</li><li>Books</li></ul>
</aside>

<main class="grid">
  <!-- row 1 -->
  <article class="card"><div class="card-image img-mala" role="img" aria-label="Coiled wooden mala beads"></div>
    <div class="card-body"><div class="card-title">Mala</div><div class="card-price">$56.00</div>
    <div class="card-desc">Lorem ipsum dolor sit amet, consectetur adipiscing elit.</div>
    <div class="stars"><svg width="76" height="8" viewBox="0 0 76 8"><g fill="#f0d052"><path id="s" d="M4 0l1.2 2.6 2.8.3-2.1 1.9.6 2.8L4 6.2 1.5 7.6l.6-2.8L0 2.9l2.8-.3z"/><use href="#s" x="11.6"/><use href="#s" x="23.2"/><use href="#s" x="34.8"/><use href="#s" x="46.4"/></g></svg></div></div>
    <div class="btn">Add to Cart</div></article>
  <article class="card"><div class="card-image img-book" role="img" aria-label="Colourful chakra guide book cover"></div>
    <div class="card-body"><div class="card-title">Guide to Chakras</div><div class="card-price">$56.00</div>
    <div class="card-desc">Lorem ipsum dolor sit amet, consectetur adipiscing elit.</div>
    <div class="stars"><svg width="76" height="8" viewBox="0 0 76 8"><g fill="#f0d052"><use href="#s"/><use href="#s" x="11.6"/><use href="#s" x="23.2"/><use href="#s" x="34.8"/><use href="#s" x="46.4"/></g></svg></div></div>
    <div class="btn">Add to Cart</div></article>
  <article class="card"><div class="card-image img-bracelet" role="img" aria-label="Open hand with amethyst crystal and beaded bracelets"></div>
    <div class="card-body"><div class="card-title">Crystal Bracelet</div><div class="card-price">$56.00</div>
    <div class="card-desc">Lorem ipsum dolor sit amet, consectetur adipiscing elit.</div>
    <div class="stars"><svg width="76" height="8" viewBox="0 0 76 8"><g fill="#f0d052"><use href="#s"/><use href="#s" x="11.6"/><use href="#s" x="23.2"/><use href="#s" x="34.8"/><use href="#s" x="46.4"/></g></svg></div></div>
    <div class="btn">Add to Cart</div></article>
  <!-- row 2 -->
  <article class="card"><div class="card-image img-mala" role="img" aria-label="Coiled wooden mala beads"></div>
    <div class="card-body"><div class="card-title">Mala</div><div class="card-price">$56.00</div>
    <div class="card-desc">Lorem ipsum dolor sit amet, consectetur adipiscing elit.</div>
    <div class="stars"><svg width="76" height="8" viewBox="0 0 76 8"><g fill="#f0d052"><use href="#s"/><use href="#s" x="11.6"/><use href="#s" x="23.2"/><use href="#s" x="34.8"/><use href="#s" x="46.4"/></g></svg></div></div>
    <div class="btn">Add to Cart</div></article>
  <article class="card"><div class="card-image img-book" role="img" aria-label="Colourful chakra guide book cover"></div>
    <div class="card-body"><div class="card-title">Guide to Chakras</div><div class="card-price">$56.00</div>
    <div class="card-desc">Lorem ipsum dolor sit amet, consectetur adipiscing elit.</div>
    <div class="stars"><svg width="76" height="8" viewBox="0 0 76 8"><g fill="#f0d052"><use href="#s"/><use href="#s" x="11.6"/><use href="#s" x="23.2"/><use href="#s" x="34.8"/><use href="#s" x="46.4"/></g></svg></div></div>
    <div class="btn">Add to Cart</div></article>
  <article class="card"><div class="card-image img-bracelet" role="img" aria-label="Open hand with amethyst crystal and beaded bracelets"></div>
    <div class="card-body"><div class="card-title">Crystal Bracelet</div><div class="card-price">$56.00</div>
    <div class="card-desc">Lorem ipsum dolor sit amet, consectetur adipiscing elit.</div>
    <div class="stars"><svg width="76" height="8" viewBox="0 0 76 8"><g fill="#f0d052"><use href="#s"/><use href="#s" x="11.6"/><use href="#s" x="23.2"/><use href="#s" x="34.8"/><use href="#s" x="46.4"/></g></svg></div></div>
    <div class="btn">Add to Cart</div></article>
  <!-- row 3 -->
  <article class="card"><div class="card-image img-mala" role="img" aria-label="Coiled wooden mala beads"></div>
    <div class="card-body"><div class="card-title">Mala</div><div class="card-price">$56.00</div>
    <div class="card-desc">Lorem ipsum dolor sit amet, consectetur adipiscing elit.</div>
    <div class="stars"><svg width="76" height="8" viewBox="0 0 76 8"><g fill="#f0d052"><use href="#s"/><use href="#s" x="11.6"/><use href="#s" x="23.2"/><use href="#s" x="34.8"/><use href="#s" x="46.4"/></g></svg></div></div>
    <div class="btn">Add to Cart</div></article>
  <article class="card"><div class="card-image img-book" role="img" aria-label="Colourful chakra guide book cover"></div>
    <div class="card-body"><div class="card-title">Guide to Chakras</div><div class="card-price">$56.00</div>
    <div class="card-desc">Lorem ipsum dolor sit amet, consectetur adipiscing elit.</div>
    <div class="stars"><svg width="76" height="8" viewBox="0 0 76 8"><g fill="#f0d052"><use href="#s"/><use href="#s" x="11.6"/><use href="#s" x="23.2"/><use href="#s" x="34.8"/><use href="#s" x="46.4"/></g></svg></div></div>
    <div class="btn">Add to Cart</div></article>
  <article class="card"><div class="card-image img-bracelet" role="img" aria-label="Open hand with amethyst crystal and beaded bracelets"></div>
    <div class="card-body"><div class="card-title">Crystal Bracelet</div><div class="card-price">$56.00</div>
    <div class="card-desc">Lorem ipsum dolor sit amet, consectetur adipiscing elit.</div>
    <div class="stars"><svg width="76" height="8" viewBox="0 0 76 8"><g fill="#f0d052"><use href="#s"/><use href="#s" x="11.6"/><use href="#s" x="23.2"/><use href="#s" x="34.8"/><use href="#s" x="46.4"/></g></svg></div></div>
    <div class="btn">Add to Cart</div></article>
</main>

<footer class="footer">
  <div class="footer-brand"><div class="brand-mark"></div><div class="brand-name">Lumenara</div></div>
  <p class="footer-about">Lorem ipsum dolor sit amet, consectetur adipiscing elit, sed do eiusmod tempor</p>
  <div class="footer-rule"></div>
  <p class="copyright">© 2022 Lumenara. All Rights Reserved.</p>
  <div class="footer-col" style="left:306px"><h4>Quick Links</h4><div class="rule"></div>
    <ul><li>Events</li><li>About Us</li><li>Synergise</li><li>Wisdom</li><li>Shop</li></ul></div>
  <div class="footer-col" style="left:402px"><h4>Company</h4><div class="rule"></div>
    <ul><li>Terms of Use</li><li>Privacy Policy</li><li>Account</li><li>Cart</li><li>Orders</li></ul></div>
  <div class="footer-col" style="left:496px;top:36px"><h4>Follow Us</h4><div class="rule"></div>
    <div class="socials"><span></span><span></span><span></span><span></span></div></div>
</footer>
</body>
</html>
```